Design Website appearance

Seeking someone to provide ideas on matters of color and contrast for the current design of the website.
Ideas top menu types and menu navigation.

https://www.filevarko.net/s/7kq4mwtzpe9bhxd/Esqueleto%20de%20Interface.pdf

Target Market(s)

We sell consulting services Information Systems for medium and small businesses.

```html
<!DOCTYPE html>
<html lang="es">
<head>
<meta charset="utf-8">
<title>Arbor Point Consulting</title>
<link href="https://fonts.googleapis.com/css2?family=Arimo:wght@400;700&display=swap" rel="stylesheet">
<style>
:root{
  --page-outer:#ffffff;
  --topbar:#555a5f;
  --body-bg:#eeeee4;
  --body-glow:#f7f7f1;
  --orange:#e0661a;
  --orange-light:#f0900f;
  --red:#d24418;
  --card-top:#fb8262;
  --card-bottom:#d8451f;
  --band:#d63f1c;
  --band-dark:#b02e10;
  --text-dark:#222222;
  --text-mid:#555555;
  --white:#ffffff;
  --dot-grey:#555a5f;
}
*{margin:0;padding:0;box-sizing:border-box}
html,body{width:1200px;height:900px;overflow:hidden;background:var(--page-outer)}
body{font-family:"Arimo",Arial,sans-serif;position:relative}
.site{position:absolute;left:141px;top:0;width:917px;height:900px;
  background:radial-gradient(ellipse at 50% 35%,var(--body-glow),var(--body-bg) 70%);overflow:hidden}
.abs{position:absolute}
.topbar{left:0;top:0;width:917px;height:27px;background:var(--topbar)}
.social{position:absolute;top:7px;display:flex;gap:8px;right:100px}
.social span{width:13px;height:13px;border-radius:2px;background:#e8e8e8;display:block}
.logo{left:99px;top:45px;font-size:20px;font-weight:700;color:var(--red);letter-spacing:.3px}
.nav{top:52px;font-size:11px;color:var(--text-dark)}
.nav a{position:absolute;white-space:nowrap;color:inherit;text-decoration:none}
.nav .active{color:var(--red)}
.search{left:659px;top:48px;width:159px;height:21px;display:flex}
.search-field{flex:1;background:var(--white);font-size:6px;color:var(--orange);padding:7px 6px;border:1px solid #e6e6e0}
.search-btn{width:21px;background:var(--orange);display:flex;align-items:center;justify-content:center}
.hero{left:99px;top:91px;width:718px;height:342px;
  background:linear-gradient(100deg,#cfd6db 0%,#e6e9ea 40%,#c9ccd0 65%,#e9eef2 100%)}
.hero-title{left:138px;top:325px;font-size:35px;line-height:1;white-space:nowrap}
.hero-title b{color:var(--red)}
.hero-title span{color:var(--orange-light)}
.hero-sub{left:167px;top:358px;font-size:20px;color:#111;white-space:nowrap}
.hero-btn{left:284px;top:387px;width:95px;height:24px;border-radius:6px;
  background:linear-gradient(#e03a2c,#b51a12);color:var(--white);font-size:11px;font-weight:700;
  display:flex;align-items:center;justify-content:center;letter-spacing:.3px;box-shadow:0 1px 2px rgba(0,0,0,.35)}
.dots{left:733px;top:406px;display:flex;gap:5px}
.dots span{width:14px;height:14px;border-radius:50%;background:var(--dot-grey)}
.dots .on{background:var(--red)}
.band{left:0;top:760px;width:917px;height:97px;background:var(--band)}
.bottombar{left:0;top:857px;width:917px;height:43px;background:var(--band-dark)}
.panel{left:99px;top:446px;width:719px;height:370px;background:var(--white);border-radius:8px}
.cards{left:116px;top:464px;width:687px;height:165px;border-radius:4px;
  background:linear-gradient(var(--card-top),var(--card-bottom));display:flex}
.card{position:relative;height:100%;border-right:2px solid rgba(255,255,255,.35)}
.card:last-child{border-right:none}
.card-icon{position:absolute;left:24px;top:14px}
.card h3{position:absolute;left:69px;top:25px;font-size:18px;font-weight:400;color:var(--white);white-space:nowrap}
.card p{position:absolute;left:25px;top:60px;width:184px;font-size:11px;line-height:12.6px;color:var(--white)}
.pill{position:absolute;left:26px;top:124px;width:89px;height:20px;border-radius:10px;
  background:linear-gradient(#a9a9a9,#6f6f6f);color:var(--white);font-size:11px;display:flex;align-items:center;padding-left:22px}
.pill::before{content:"";position:absolute;left:4px;top:3px;width:14px;height:14px;border-radius:50%;
  background:radial-gradient(circle at 40% 35%,#ffe066,#f39a00)}
.feature{position:absolute;top:641px;width:210px}
.feature h4{font-size:18px;font-weight:400;color:var(--text-mid)}
.thumb{margin:8px 0 0 1px;width:201px;height:67px;background:linear-gradient(#dfe6ea 0%,#c8cfd4 55%,#2a3440 56%,#3c4a5c 100%)}
.feature p{margin-top:7px;width:210px;font-size:11px;line-height:12.6px;color:#444}
.feature a{display:block;margin-top:3px;font-size:8px;color:var(--red);text-decoration:underline}
.footer-nav{left:0;width:917px;top:831px;text-align:center;font-size:11px;color:var(--white)}
.footer-nav a{color:inherit;text-decoration:none;margin:0 10px}
.copyright{left:99px;top:873px;font-size:11px;color:var(--white)}
</style>
</head>
<body>
<div class="site">
  <div class="abs topbar">
    <div class="social" aria-label="Redes sociales"><span></span><span></span><span></span><span></span><span></span></div>
  </div>

  <div class="abs logo">ARBORPOINT</div>

  <nav class="abs nav">
    <a class="active" style="left:427px">Inicio</a>
    <a style="left:475px">Acerca de nosotros</a>
    <a style="left:590px">Contáctenos</a>
  </nav>
  <div class="abs search">
    <div class="search-field">Enter your search term...</div>
    <div class="search-btn"><svg width="9" height="9" viewBox="0 0 9 9"><circle cx="3.5" cy="3.5" r="2.5" fill="none" stroke="#fff" stroke-width="1.4"/><path d="M5.3 5.3 8 8" stroke="#fff" stroke-width="1.6"/></svg></div>
  </div>

  <div class="abs hero" role="img" aria-label="Fotografía: mujer sonriente junto a un portátil en una oficina luminosa"></div>
  <div class="abs hero-title"><b>REAL</b><span>Solutions</span></div>
  <div class="abs hero-sub">FOR YOUR SUCCESS!</div>
  <div class="abs hero-btn">LEARN MORE</div>
  <div class="abs dots"><span class="on"></span><span></span><span></span><span></span></div>

  <div class="abs band"></div>
  <div class="abs bottombar"></div>

  <div class="abs panel"></div>
  <div class="abs cards">
    <div class="card" style="width:228px">
      <svg class="card-icon" width="36" height="36" viewBox="0 0 36 36"><path d="M2 32h32l-4 3H2z" fill="#cfd8e0"/><rect x="5" y="18" width="5" height="14" fill="#2f6fd1"/><rect x="12" y="10" width="5" height="22" fill="#3d86e8"/><rect x="19" y="4" width="5" height="28" fill="#2f6fd1"/><rect x="26" y="14" width="5" height="18" fill="#3d86e8"/></svg>
      <h3>Lorem ipsum</h3>
      <p>dolor sit amet, consectetur adipisicing elit, sed do eiusmod tempor incididunt ut labore et dolore magna aliqua.</p>
      <div class="pill">Learn More</div>
    </div>
    <div class="card" style="width:226px">
      <svg class="card-icon" width="36" height="36" viewBox="0 0 36 36"><path d="M2 32h32l-4 3H2z" fill="#cfd8e0"/><rect x="5" y="18" width="5" height="14" fill="#2f6fd1"/><rect x="12" y="10" width="5" height="22" fill="#3d86e8"/><rect x="19" y="4" width="5" height="28" fill="#2f6fd1"/><rect x="26" y="14" width="5" height="18" fill="#3d86e8"/></svg>
      <h3>Lorem ipsum</h3>
      <p>dolor sit amet, consectetur adipisicing elit, sed do eiusmod tempor incididunt ut labore et dolore magna aliqua.</p>
      <div class="pill">Learn More</div>
    </div>
    <div class="card" style="width:233px">
      <svg class="card-icon" style="left:20px" width="36" height="36" viewBox="0 0 36 36"><path d="M2 32h32l-4 3H2z" fill="#cfd8e0"/><rect x="5" y="18" width="5" height="14" fill="#2f6fd1"/><rect x="12" y="10" width="5" height="22" fill="#3d86e8"/><rect x="19" y="4" width="5" height="28" fill="#2f6fd1"/><rect x="26" y="14" width="5" height="18" fill="#3d86e8"/></svg>
      <h3 style="left:64px">Lorem ipsum</h3>
      <p style="left:20px">dolor sit amet, consectetur adipisicing elit, sed do eiusmod tempor incididunt ut labore et dolore magna aliqua.</p>
      <div class="pill" style="left:21px">Learn More</div>
    </div>
  </div>

  <div class="feature" style="left:128px">
    <h4>Lorem ipsum</h4>
    <div class="thumb" role="img" aria-label="Fotografía: hombre de negocios con portátil en una sala de espera"></div>
    <p>dolor sit amet, consectetur adipisicing elit, sed do eiusmod tempor incididunt ut labore et dolore magna aliqua.</p>
    <a>READ MORE</a>
  </div>
  <div class="feature" style="left:356px">
    <h4>Lorem ipsum</h4>
    <div class="thumb" role="img" aria-label="Fotografía: hombre de negocios con portátil en una sala de espera"></div>
    <p>dolor sit amet, consectetur adipisicing elit, sed do eiusmod tempor incididunt ut labore et dolore magna aliqua.</p>
    <a>READ MORE</a>
  </div>
  <div class="feature" style="left:584px">
    <h4>Lorem ipsum</h4>
    <div class="thumb" role="img" aria-label="Fotografía: hombre de negocios con portátil en una sala de espera"></div>
    <p>dolor sit amet, consectetur adipisicing elit, sed do eiusmod tempor incididunt ut labore et dolore magna aliqua.</p>
    <a>READ MORE</a>
  </div>

  <nav class="abs footer-nav"><a>Inicio</a><a>Acerca de nosotros</a><a>Contáctenos</a></nav>
  <div class="abs copyright">Copyright© Arbor Point Consulting. All rights reserved.</div>
</div>
</body>
</html>
```